Corvane Equipment and Trade, LLC

Would like an e-commerce website started

tallow-creek gearworks website is a business that is almost exactly like ours...I like how in the front of the website...their lines flash across the bottom...I have attached our line card to add some of ours

we are velk certified...I would like that to show...... attached logo

also attached our logo

```html
<!DOCTYPE html>
<html lang="en">
<head>
<meta charset="utf-8">
<title>Corvane Equipment and Trade, LLC</title>
<link href="https://fonts.googleapis.com/css2?family=Open+Sans:wght@400;600;700&family=Montserrat:wght@400;500;600&display=swap" rel="stylesheet">
<style>
:root{
  --green:#5b9b2e;
  --green-dark:#4a8424;
  --ink:#1b1b1b;
  --text:#555;
  --line:#e3e3e3;
  --footer:#000;
  --white:#fff;
}
*{box-sizing:border-box;margin:0;padding:0}
html,body{width:1200px;height:4018px;overflow:hidden}
body{position:relative;background:var(--white);font-family:"Montserrat",sans-serif;color:var(--text)}
.abs{position:absolute}
.topbar{left:0;top:0;width:1200px;height:4px;background:var(--green)}
.brand{display:flex;align-items:center;gap:10px;font-family:"Open Sans",sans-serif;font-weight:700;color:var(--ink)}
.brand .mark{width:24px;height:24px;background:var(--ink);flex:none}
.brand .name{display:block}
.header-brand{left:106px;top:26px;font-size:18px;line-height:22px}
.header-brand .name{width:200px}
.footer-brand{left:98px;top:124px;font-size:22px;line-height:28px;color:#fff}
.footer-brand .name{width:240px}
.footer-brand .mark{background:#fff;width:28px;height:28px}
.nav{left:458px;top:47px;display:flex;gap:36px;font-size:15px;color:#333}
.nav .active{color:var(--green);font-weight:600}
.btn{display:inline-flex;align-items:center;gap:10px;background:var(--green);color:#fff;border-radius:24px;font-family:"Open Sans",sans-serif;font-weight:600;font-size:15px;justify-content:center}
.phone-btn{left:941px;top:28px;width:160px;height:45px}
.hero{left:0;top:97px;width:1200px;height:600px;background:linear-gradient(90deg,#15181c 0%,#252a30 35%,#5b4030 60%,#8a5a35 75%,#2f3238 100%)}
.hero h1{position:absolute;left:100px;top:118px;width:560px;font-family:"Open Sans",sans-serif;font-weight:700;font-size:54px;line-height:62px;color:#fff}
.hero p{position:absolute;left:100px;top:325px;width:420px;font-size:16px;line-height:31px;color:#fff}
.hero .btn{position:absolute;left:100px;top:406px;width:160px;height:46px}
.section-title{font-family:"Open Sans",sans-serif;font-weight:700;font-size:32px;color:var(--ink)}
.section-title span{color:var(--green)}
.divider{left:0;width:1200px;height:1px;background:var(--line)}
.brands-title{left:0;top:770px;width:1200px;text-align:center;font-family:"Open Sans",sans-serif;font-weight:700;font-size:26px;color:var(--ink)}
.brands-rule{left:270px;top:839px;width:660px;height:1px;background:linear-gradient(90deg,transparent,#ddd,transparent)}
.logo-card{top:898px;width:180px;height:95px;border:1px solid #ececec;display:flex;align-items:center;justify-content:center;font-family:"Open Sans",sans-serif;font-weight:700;font-size:20px;background:#fff}
.logo-card.raised{box-shadow:0 8px 20px rgba(0,0,0,.15);border-color:#f2f2f2}
.photo{display:block}
.frame{border:2px solid var(--green)}
.body-copy{font-size:15px;line-height:31px;color:var(--text)}
.service-item{left:638px;width:464px}
.service-item h3{display:flex;align-items:center;gap:16px;font-family:"Open Sans",sans-serif;font-weight:600;font-size:17px;color:var(--ink);margin-bottom:16px}
.service-item li{list-style:none;display:flex;align-items:center;gap:14px;font-size:15px;line-height:31px;color:var(--text)}
.service-sep{left:638px;width:462px;height:1px;background:var(--line)}
.product-caption{top:2835px;width:232px;text-align:center;font-family:"Open Sans",sans-serif;font-weight:600;font-size:19px;color:var(--ink)}
.circle-arrow{width:28px;height:28px}
.contact-row{left:98px;display:flex;gap:18px}
.contact-icon{width:56px;height:56px;border-radius:50%;background:var(--green);display:flex;align-items:center;justify-content:center;flex:none}
.contact-row .info{font-size:15px;line-height:31px;color:#333;padding-top:2px}
.contact-row b{font-family:"Open Sans",sans-serif;font-weight:700;color:var(--ink)}
.footer{left:0;top:3567px;width:1200px;height:451px;background:var(--footer)}
.footer h4{font-family:"Open Sans",sans-serif;font-weight:700;font-size:21px;color:#fff;margin-bottom:10px}
.footer li{list-style:none;display:flex;align-items:center;gap:14px;font-size:14px;line-height:31px;color:#fff}
.social{display:flex;gap:17px}
.social span{width:28px;height:28px;border-radius:50%;background:var(--green)}
.badge{background:#3a2a8c;border:3px solid #fff;outline:1px solid #3a2a8c}
.copyright{left:0;top:3958px;width:1200px;text-align:center;font-size:14px;color:#fff}
</style>
</head>
<body>
<svg width="0" height="0" style="position:absolute">
  <defs>
    <symbol id="arrow" viewBox="0 0 16 16"><path d="M2 8h10M8 3l5 5-5 5" fill="none" stroke="currentColor" stroke-width="2.6" stroke-linecap="round" stroke-linejoin="round"/></symbol>
    <symbol id="phone" viewBox="0 0 24 24"><path d="M6.6 10.8a15 15 0 0 0 6.6 6.6l2.2-2.2c.3-.3.7-.4 1-.2 1.1.4 2.3.6 3.6.6.6 0 1 .4 1 1V20c0 .6-.4 1-1 1A17 17 0 0 1 3 4c0-.6.4-1 1-1h3.5c.6 0 1 .4 1 1 0 1.3.2 2.5.6 3.6.1.3 0 .7-.2 1z" fill="currentColor"/></symbol>
  </defs>
</svg>

<div class="abs topbar"></div>
<header>
  <div class="abs brand header-brand"><span class="mark"></span><span class="name">Corvane Equipment &amp; Trade, LLC</span></div>
  <nav class="abs nav"><span class="active">Home</span><span>About Us</span><span>Services</span><span>Products</span><span>Contact Us</span></nav>
  <a class="abs btn phone-btn"><svg width="14" height="14" style="color:#fff"><use href="#phone"/></svg>555-014-2290</a>
</header>

<section class="abs hero" role="img" aria-label="Warehouse aisle with stacked cardboard boxes on a pallet">
  <h1>Welcome To Corvane Equipment &amp; Trade, LLC</h1>
  <p>Lorem ipsum dolor sit amet, consectetur adipiscing elit, sed do eiusmod dolore magna aliqua.</p>
  <a class="btn">Get Started <svg width="14" height="14"><use href="#arrow"/></svg></a>
</section>

<section class="brands">
  <h2 class="abs brands-title">Serving Industrial &amp; Agricultural needs with the Best Brands in the Industry.</h2>
  <div class="abs brands-rule"></div>
  <svg class="abs" style="left:50px;top:936px" width="14" height="20"><path d="M11 2 3 10l8 8" fill="none" stroke="#999" stroke-width="1.5"/></svg>
  <div class="abs logo-card" style="left:98px;color:#2a5aa8">Ravelin</div>
  <div class="abs logo-card" style="left:304px;color:#d0202a">Dorrik Chain</div>
  <div class="abs logo-card raised" style="left:511px;color:#1d3e7a">Brevatto</div>
  <div class="abs logo-card" style="left:717px;color:#0f6a63">Plenmoor</div>
  <div class="abs logo-card" style="left:923px;color:#d0202a">Kestrow</div>
  <svg class="abs" style="left:1136px;top:936px" width="14" height="20"><path d="M3 2l8 8-8 8" fill="none" stroke="#333" stroke-width="1.5"/></svg>
</section>

<div class="abs divider" style="top:1077px"></div>

<section class="about">
  <h2 class="abs section-title" style="left:98px;top:1168px">About <span>Us</span></h2>
  <p class="abs body-copy" style="left:98px;top:1227px;width:470px">Lorem ipsum dolor sit amet, consectetur adipiscing elit, sed do eiusmod tempor incididunt ut labore et dolore magna aliqua. Ut enim ad minim veniam, quis nostrud exercitation ullamco laboris nisi ut aliquip ex ea commodo consequat. Duis aute irure dolor in reprehenderit in voluptate velit esse cillum dolore eu fugiat nulla pariatur.</p>
  <p class="abs body-copy" style="left:98px;top:1443px;width:470px">Excepteur sint occaecat cupidatat non proident, sunt in culpa qui officia deserunt mollit anim id est laborum.</p>
  <a class="abs btn" style="left:98px;top:1532px;width:160px;height:47px">Read More <svg width="14" height="14"><use href="#arrow"/></svg></a>
  <div class="abs frame" style="left:623px;top:1177px;width:471px;height:413px"></div>
  <div class="abs photo" role="img" aria-label="Lab technician in safety glasses inspecting a circuit board under a lamp" style="left:634px;top:1168px;width:467px;height:411px;background:linear-gradient(135deg,#0c2236,#1e5a7c 45%,#0e2a40)"></div>
</section>

<div class="abs divider" style="top:1690px"></div>

<section class="services">
  <div class="abs photo" role="img" aria-label="Workers in hard hats walking through a refinery plant" style="left:98px;top:1789px;width:467px;height:237px;background:linear-gradient(135deg,#5f6b74,#2e3740 60%,#8a7a40)"></div>
  <div class="abs photo" role="img" aria-label="Engineer at a computer working on a 3D part model" style="left:98px;top:2050px;width:224px;height:261px;background:linear-gradient(135deg,#e8eaec,#9aa3ab 60%,#3a3e44)"></div>
  <div class="abs photo" role="img" aria-label="Worker in a yellow hard hat and hi-vis jacket" style="left:340px;top:2050px;width:223px;height:261px;background:linear-gradient(160deg,#7a7f86,#3d4c68 55%,#c65a25)"></div>

  <h2 class="abs section-title" style="left:636px;top:1789px">Our <span>Services</span></h2>
  <p class="abs body-copy" style="left:638px;top:1846px;width:450px">Excepteur sint occaecat cupidatat non proident, sunt in culpa qui officia deserunt mollit anim id est laborum.</p>

  <div class="abs service-item" style="top:1926px">
    <h3><svg width="38" height="32" viewBox="0 0 38 32"><circle cx="19" cy="13" r="9" fill="none" stroke="#5b9b2e" stroke-width="1.5"/><path d="M4 30h30" stroke="#5b9b2e" stroke-width="1.5"/></svg>Computer-Aided Design</h3>
    <ul><li><svg width="14" height="14" style="color:var(--green)"><use href="#arrow"/></svg>Lorem ipsum dolor sit amet</li>
    <li><svg width="14" height="14" style="color:var(--green)"><use href="#arrow"/></svg>consectetur adipiscing elit, sed do eiusmod tempor</li></ul>
  </div>
  <div class="abs service-sep" style="top:2050px"></div>
  <div class="abs service-item" style="top:2068px">
    <h3><svg width="38" height="32" viewBox="0 0 38 32"><rect x="4" y="6" width="30" height="20" rx="3" fill="none" stroke="#5b9b2e" stroke-width="1.5"/><path d="M10 16h18" stroke="#5b9b2e" stroke-width="1.5"/></svg>Fabrication and installation</h3>
    <ul><li><svg width="14" height="14" style="color:var(--green)"><use href="#arrow"/></svg>Lorem ipsum dolor sit amet</li>
    <li><svg width="14" height="14" style="color:var(--green)"><use href="#arrow"/></svg>consectetur adipiscing elit, sed do eiusmod tempor</li></ul>
  </div>
  <div class="abs service-sep" style="top:2192px"></div>
  <div class="abs service-item" style="top:2210px">
    <h3><svg width="34" height="32" viewBox="0 0 34 32"><rect x="6" y="3" width="22" height="27" rx="2" fill="none" stroke="#5b9b2e" stroke-width="1.5"/><path d="M11 11h12M11 17h12M11 23h8" stroke="#5b9b2e" stroke-width="1.5"/></svg>Plant surveys</h3>
    <ul><li><svg width="14" height="14" style="color:var(--green)"><use href="#arrow"/></svg>Lorem ipsum dolor sit amet</li>
    <li><svg width="14" height="14" style="color:var(--green)"><use href="#arrow"/></svg>consectetur adipiscing elit, sed do eiusmod tempor</li></ul>
  </div>
</section>

<div class="abs divider" style="top:2428px"></div>

<section class="products">
  <h2 class="abs section-title" style="left:0;top:2502px;width:1200px;text-align:center">Our <span>Products</span></h2>
  <svg class="abs circle-arrow" style="left:43px;top:2699px" viewBox="0 0 28 28"><circle cx="14" cy="14" r="12.5" fill="none" stroke="#999"/><path d="M16 8l-6 6 6 6" fill="none" stroke="#999" stroke-width="1.5"/></svg>
  <div class="abs photo" role="img" aria-label="Yellow mobile crane at a construction site at sunset" style="left:98px;top:2573px;width:232px;height:243px;background:linear-gradient(180deg,#b9c2c8,#d9a55a 55%,#4d4a3f)"></div>
  <div class="abs photo" role="img" aria-label="Container port with red gantry cranes" style="left:356px;top:2573px;width:231px;height:243px;background:linear-gradient(180deg,#c9ccd0,#b43a32 45%,#3a6a8a)"></div>
  <div class="abs photo" role="img" aria-label="Barista pouring coffee through a filter" style="left:614px;top:2573px;width:231px;height:243px;background:linear-gradient(135deg,#cfcfcf,#6b5a4a 50%,#2e2620)"></div>
  <div class="abs photo" role="img" aria-label="Tower crane over a building at dusk" style="left:871px;top:2573px;width:231px;height:243px;background:linear-gradient(180deg,#5e7fa6,#c99370 60%,#3a3d44)"></div>
  <svg class="abs circle-arrow" style="left:1134px;top:2699px" viewBox="0 0 28 28"><circle cx="14" cy="14" r="12.5" fill="none" stroke="#222"/><path d="M12 8l6 6-6 6" fill="none" stroke="#222" stroke-width="1.5"/></svg>
  <p class="abs product-caption" style="left:98px">Cranes</p>
  <p class="abs product-caption" style="left:356px">Crane Controls</p>
  <p class="abs product-caption" style="left:614px">Filters</p>
  <p class="abs product-caption" style="left:871px">Hoists</p>
</section>

<div class="abs divider" style="top:2940px"></div>

<section class="location">
  <h2 class="abs section-title" style="left:98px;top:3030px">Memphis <span>Location</span></h2>
  <div class="abs contact-row" style="top:3102px">
    <span class="contact-icon"><svg width="18" height="18" style="color:#fff"><use href="#phone"/></svg></span>
    <div class="info"><b>Fax:</b> 555-014-2291<br><b>Phone:</b> 555-014-2290</div>
  </div>
  <div class="abs contact-row" style="top:3196px">
    <span class="contact-icon"><svg width="18" height="14" viewBox="0 0 18 14"><rect x="0" y="0" width="18" height="14" rx="1.5" fill="#fff"/><path d="M1 1l8 6 8-6" fill="none" stroke="#5b9b2e" stroke-width="1.5"/></svg></span>
    <div class="info"><b>Email:</b><br>owen@corvanetrade.com</div>
  </div>
  <div class="abs contact-row" style="top:3290px">
    <span class="contact-icon"><svg width="16" height="20" viewBox="0 0 16 20"><path d="M8 0a8 8 0 0 0-8 8c0 6 8 12 8 12s8-6 8-12a8 8 0 0 0-8-8z" fill="#fff"/><circle cx="8" cy="8" r="3" fill="#5b9b2e"/></svg></span>
    <div class="info"><b>Location:</b><br>Owen Marlett 812 Halden Row, Brookfall, TN<br>38100</div>
  </div>
  <a class="abs btn" style="left:98px;top:3420px;width:160px;height:46px">Contact Us <svg width="14" height="14"><use href="#arrow"/></svg></a>
  <div class="abs frame" style="left:623px;top:3037px;width:471px;height:413px"></div>
  <div class="abs photo" role="img" aria-label="Two engineers in hard hats reviewing data on a laptop" style="left:634px;top:3028px;width:467px;height:411px;background:linear-gradient(135deg,#c8ccd0,#3a5a9a 45%,#e07a2a 80%)"></div>
</section>

<footer class="abs footer">
  <div class="abs brand footer-brand"><span class="mark"></span><span class="name">Corvane Equipment &amp; Trade, LLC</span></div>
  <div class="abs social" style="left:129px;top:241px"><span></span><span></span><span></span><span></span></div>
  <div class="abs" style="left:438px;top:103px">
    <h4>Quick Links</h4>
    <ul>
      <li><svg width="13" height="13"><use href="#arrow" style="color:#fff"/></svg>Menu</li>
      <li><svg width="13" height="13"><use href="#arrow" style="color:#fff"/></svg>Home</li>
      <li><svg width="13" height="13"><use href="#arrow" style="color:#fff"/></svg>Our Services</li>
      <li><svg width="13" height="13"><use href="#arrow" style="color:#fff"/></svg>Features</li>
      <li><svg width="13" height="13"><use href="#arrow" style="color:#fff"/></svg>About Us</li>
      <li><svg width="13" height="13"><use href="#arrow" style="color:#fff"/></svg>Contact</li>
    </ul>
  </div>
  <div class="abs" style="left:637px;top:103px">
    <h4>Other Links</h4>
    <ul>
      <li><svg width="13" height="13"><use href="#arrow" style="color:#fff"/></svg>E-books</li>
      <li><svg width="13" height="13"><use href="#arrow" style="color:#fff"/></svg>FAQ</li>
      <li><svg width="13" height="13"><use href="#arrow" style="color:#fff"/></svg>Videos</li>
      <li><svg width="13" height="13"><use href="#arrow" style="color:#fff"/></svg>Security and Privacy</li>
    </ul>
  </div>
  <div class="abs badge" style="left:892px;top:104px;width:209px;height:82px" role="img" aria-label="Velk certification badge"></div>
  <div class="abs" style="left:98px;top:371px;width:1004px;height:1px;background:#555"></div>
</footer>
<p class="abs copyright">Copyrights@2024.Corvane.All Rights Reserved</p>
</body>
</html>
```